Specialist Medical practice after professional trifold flyer design for patient information brochure

I am the Director of the Hollowbrook Clinic, a specialist medial and surgical practice in Australia. I am after a professional design of a patient information trifold flyer that can be used for web distribution or for commercial printing for upcoming educational event. The design would need to allow change of images and text to be used as template for future topics but have a common brand look across them. Colours would follow the logo, but primarily blue colours for the hollowbrook theme. The inside text needs to be clearly contrasted to the background for easy reading, as often elderly patients. The design would make use of curves or circles, but open for hexagonal, triangle square vector components. I have included an outline for the initial brochure and included images to include. Other stock background images can be used if they increase the impact of the design over included. A winning design is also one that could be modified to a 4 page bi-fold brochure

Target Market(s)

This will be provided to patients in GP practices, podiatry clinics, radiological practices. Aimed at patients to read and be compelled to look to site or get consultation with me

Industry/Entity Type

Medical

Font styles to use
Serif
Sans Serif

Colors
33a6d7
0355a3
86cfc6
cedeed
0292cd
85cae6

Requirements
Must have
• The front cover needs to engage the patient to pick up and read- yes I have a painful ankle and want to find out more. the goal for the inside is to provide the options but be able to direct to website for more info - website currently undergoing upgrade. After professional modern look. Not bright contrasting colours like many advertising brochures. Needs to able to have images and text changed but following same look to create new topics
Nice to have
• The focus is a Tri-fold brochure. Nice to be able to modify to bifold. A winning design would even offer both, or submit separate bifold and trifold. I am open to different versions of similar look. (eg option of brochure with curved elements, triangular or square, or hexagonal.
Should not have
• To many contrasting colours. Text must be easily read on background, either white or coloured background texture with transparency

```html
<!DOCTYPE html>
<html lang="en">
<head>
<meta charset="utf-8">
<title>Hollowbrook Clinic – My Painful Ankle trifold</title>
<link href="https://fonts.googleapis.com/css2?family=Source+Sans+3:ital,wght@0,300;0,400;0,600;0,700;1,400;1,600;1,700&family=Lora:wght@600&display=swap" rel="stylesheet">
<style>
:root{
  --navy:#0a3f96;
  --blue:#0355a3;
  --sky:#0292cd;
  --aqua:#33a6d7;
  --pale:#85cae6;
  --mist:#cedeed;
  --ink:#2b2b2b;
  --page:#e6e8eb;
  --white:#ffffff;
}
*{box-sizing:border-box;margin:0;padding:0}
html,body{width:1200px;height:1200px;overflow:hidden;background:var(--page)}
body{font-family:"Source Sans 3",Arial,sans-serif;color:var(--ink);position:relative}
.spread{position:absolute;left:220px;width:760px;height:588px;display:grid;grid-template-columns:repeat(3,1fr);box-shadow:0 6px 14px rgba(0,0,0,.25);overflow:hidden}
.spread--inside{top:6px}
.spread--outside{top:606px}
.panel{position:relative;overflow:hidden;font-size:8.6px;line-height:1.38}
.panel p{margin-bottom:8px;text-align:justify}
.panel--white{background:var(--white)}
.panel--blue{background:radial-gradient(circle at 40% 30%,#1d6ed0 0%,var(--blue) 45%,var(--navy) 100%);color:var(--white)}
.ph{display:block}
.ph--xray{background:linear-gradient(135deg,#4a4a4a,#111 70%)}
.inside-strip{position:absolute;left:0;right:0;bottom:0;height:7px;background:linear-gradient(90deg,var(--navy),var(--sky),var(--navy));z-index:3}

/* inside panel 1 */
.intro{padding:20px 22px 0}
.intro__photo{position:absolute;left:0;top:0;width:135px;height:90px;background:linear-gradient(120deg,#dfeaf3,#9fbcd6);border-bottom-right-radius:70px}
.intro__lead{margin-left:120px;margin-top:28px;text-align:right!important}
.intro__xray{position:absolute;left:23px;top:318px;width:208px;height:236px}

/* inside panel 2 */
.options{padding:30px 20px 0 20px}
.options p{color:var(--white)}
.figure-row{display:flex;gap:10px;margin-top:26px}
.figure-row .ph--xray{width:115px;height:163px;flex:none}
.more{font-size:8.6px;line-height:1.35}
.more em{display:block;margin-top:10px}
.link-box{display:block;background:var(--sky);color:var(--white);font-style:italic;padding:2px 6px;border-radius:3px;line-height:1.15;margin-top:2px}
.more__title{margin-top:38px}

/* inside panel 3 */
.results{padding:30px 20px 0 22px}
.results__figure{display:flex;gap:8px;margin:4px 0 22px}
.results__figure .ph--xray{width:104px;height:120px;flex:none}
.results h3{font-size:9px;font-weight:600;margin-bottom:1px}
.results .more{color:var(--ink)}
.results .link-box{background:linear-gradient(180deg,#2a8fe0,#1066c4)}

/* outside panel 1 */
.bio{padding:24px 22px 0 24px;font-style:italic;font-size:7.4px;line-height:1.3}
.bio p{text-align:justify}
.bio__name{position:absolute;left:24px;top:120px;font-style:italic}
.bio__name strong{display:block;color:var(--sky);font-weight:400;font-size:10.5px;line-height:1}
.bio__name span{display:block;color:#777;font-size:6.6px;line-height:1.25;margin-top:3px}
.bio__portrait{position:absolute;left:78px;top:85px;width:160px;height:300px;background:linear-gradient(180deg,#f1f1f1 0%,#d9d9d9 55%,#2c2f38 56%,#1a1c22 100%);border-radius:60px 60px 0 0}
.curves{position:absolute;left:0;bottom:0;width:100%;height:100%;pointer-events:none}
.conditions{position:absolute;left:22px;right:20px;top:405px;color:var(--white);font-style:italic}
.conditions h2{font-weight:400;font-size:12px;margin-bottom:12px}
.conditions p{font-size:6.8px;line-height:1.3;color:#b9cfee;margin-bottom:10px;text-align:left}

/* outside panel 2 */
.contact{background:var(--blue)}
.contact__top{height:72px;background:linear-gradient(180deg,#3a70b8,#4e86c6);display:flex;align-items:center;padding-left:24px}
.brand{font-family:"Lora",Georgia,serif;font-weight:600;letter-spacing:.02em;display:flex;align-items:center;gap:6px;text-transform:uppercase}
.brand__dot{width:9px;height:9px;border-radius:50%;background:currentColor;flex:none}
.brand--light{color:var(--white);font-size:9px}
.contact__building{height:230px;background:linear-gradient(180deg,#7fa2cc 0%,#b5cbe2 45%,#e9eef3 70%,#6e8a62 100%)}
.contact__logo{height:120px;background:var(--white);display:flex;align-items:center;justify-content:center}
.brand--dark{color:var(--blue);font-size:15px}
.contact__info{padding:12px 18px 0 18px;color:var(--white);font-size:9px;line-height:1.15}
.info-row{display:flex;gap:10px;padding-bottom:6px;margin-bottom:7px;border-bottom:1px dashed rgba(255,255,255,.55)}
.info-row:last-child{border-bottom:none}
.info-row svg{width:11px;height:11px;flex:none;margin-top:1px}
.info-row.no-icon{padding-left:21px}
.info-row b{font-size:11.5px;letter-spacing:.02em;display:block}

/* outside panel 3 */
.cover__photo{position:absolute;left:0;top:0;width:100%;height:100%;background:linear-gradient(170deg,#c58a5d 0%,#d8b07c 30%,#c9c274 55%,#8f9e52 75%,#6a8a3c 100%)}
.cover__hook{position:absolute;right:8px;top:24px;width:140px;padding:8px 10px 8px 12px;background:rgba(255,255,255,.55);border-radius:0 0 10px 10px;line-height:1.05}
.cover__hook strong{display:block;color:var(--aqua);font-style:italic;font-weight:700;font-size:19px}
.cover__hook span{display:block;color:#555;font-weight:300;font-size:18px;margin-top:2px}
.cover__footer{position:absolute;left:0;right:0;bottom:0;top:380px;color:var(--white);padding:40px 0 0 62px}
.cover__footer .brand{font-size:11px}
.cover__titles{margin-top:26px;font-style:italic;font-weight:600;font-size:9px;line-height:1.15}
.cover__titles small{display:block;font-size:6.6px;margin-bottom:16px}
</style>
</head>
<body>

<section class="spread spread--inside" aria-label="Brochure inside spread">
  <div class="panel panel--white intro">
    <div class="intro__photo ph" role="img" aria-label="Doctor holding an ankle x-ray"></div>
    <p class="intro__lead">Ankle arthritis is a painful condition where there is loss of cartilage from the ankle joint surface. Although not as common as knee or hip arthritis, pain can be debilitating affecting quality of life.</p>
    <p>Arthritis of the joint can be caused by trauma such as fracture or recurrent instability or secondary from inflammatory conditions such as rheumatoid arthritis.</p>
    <p>Pain from the joint will occur with activity causing a limp, limiting walking speed and distance. Often there is swelling of the joint with progressive loss of motion.</p>
    <p>Diagnosis is made with examination of the ankle and weight bearing x-rays showing loss of joint space.</p>
    <div class="intro__xray ph ph--xray" role="img" aria-label="Lateral x-ray of an arthritic ankle"></div>
  </div>

  <div class="panel panel--blue options">
    <p>When pain medication, activity modification and shoe ware modification is no longer effective to control the pain then then it is worthwhile discussing with your GP for referral to Dr Martin Ellery for an opinion on further treatment. As an Orthopaedic Foot and Ankle surgeon, he will be able to assess your conditions and give advice on the best options for your treatment.</p>
    <p>The decision on the best option is based on your age, activity level, existing medical problems, previous ankle treatment and your expected outcome from treatment. In the situation of end stage arthritis options consist of either Ankle fusion or Total Ankle replacement.</p>
    <p style="margin-bottom:0">Ankle Fusion Surgery.</p>
    <p>This operation aims to stiffen the ankle joint by fusing the tibia and talus together in the optimal position for function. The common thought is that there will be no movement of the foot, and the patient will walk with a limp. The fusion only occurs at the ankle joint, leaving motion available to the surrounding joints. Although there is decreased motion, you will walk more normally after a fusion without a limp as the pain to the joint is removed.</p>
    <div class="figure-row">
      <div class="ph ph--xray" role="img" aria-label="X-ray of an ankle fusion with plate and screws"></div>
      <div class="more">
        For more information on ankle fusion, risks and recovery
        <em>visit our website :</em>
        <span class="link-box">www.hollowbrookclinic.<br>com.au/Ankle-Fusion</span>
        <div class="more__title">Total Ankle Replacement Surgery</div>
      </div>
    </div>
  </div>

  <div class="panel panel--white results">
    <p>In suitable patients there may be the option to maintain joint motion and perform a Total Ankle Replacement. Like a hip or knee replacement operation, the arthritic joint is removed and replaced with an artificial joint. Like an ankle fusion there will alleviation of the pain and limp with maintenance of the ankle joint motion. Recovery to walking post-surgery is often much sooner than with ankle fusion. Dr Martin Ellery if one of the few surgeons to have completed an international fellowship in ankle replacement surgery and has been performing the technique since 2008. He is currently performing the technique using the Kelvara Total Ankle with Tesselyn guides.</p>
    <div class="results__figure">
      <div class="ph ph--xray" role="img" aria-label="X-ray of a total ankle replacement"></div>
      <div class="more">
        For more information on ankle fusion, risks and recovery
        <em>visit our website :</em>
        <span class="link-box">www.hollowbrookclinic.<br>com.au/Ankle-<br>Replacement</span>
      </div>
    </div>
    <h3>Results of surgery</h3>
    <p>Successful surgery in the suitable patient will help resolve the pain associated with the ankle arthritis. Ankle Fusion surgery is ideal for patients with heavy labour work, allowing them to return to previous activities. There may be the risk of arthritis to surrounding joints in the future, but often this occurs many years down the track. Results from Total Ankle replacement surgery have been improving over the years, but there is known risks of loosening, cyst formation or failure of the joint over time that can occur in some patients. It is important to have a opinion from an Orthopaedic Foot and Ankle Surgeon experienced in the these procedure to determine which procedure will provide the best long term solution for you.</p>
  </div>
  <div class="inside-strip"></div>
</section>

<section class="spread spread--outside" aria-label="Brochure outside spread">
  <div class="panel panel--white">
    <div class="bio">
      <p>Dr Martin Ellery is an Australian trained Orthopaedic Surgeon who has a primary focus in the treatment of conditions of the foot and ankle. He has completed post fellowship training in Foot and Ankle surgery both locally and internationally, and continues to update himself in the latest techniques.</p>
    </div>
    <div class="bio__portrait ph" role="img" aria-label="Portrait of Dr Martin Ellery in suit and tie"></div>
    <div class="bio__name"><strong>Dr Martin<br>Ellery</strong><span>MBBS (Hons),<br>FRACS (Ortho),<br>FA (Ortho)</span></div>
    <svg class="curves" viewBox="0 0 253 588" preserveAspectRatio="none" aria-hidden="true">
      <path d="M0 290 C40 360 110 385 253 395 L253 588 L0 588 Z" fill="var(--pale)"/>
      <path d="M0 315 C40 380 120 400 253 405 L253 588 L0 588 Z" fill="var(--aqua)"/>
      <path d="M0 330 C50 395 130 412 253 412 L253 588 L0 588 Z" fill="var(--blue)"/>
    </svg>
    <div class="conditions">
      <h2>Conditions treated</h2>
      <p>Dr Ellery provides assessment and treatment of all foot and ankle conditions. He has special interest in the following:</p>
      <p>Minimally invasive treatment for bunions and toe deformities. Joint sparing procedures for arthritis or deformity, including the Solvana implant.</p>
      <p>Joint fusion procedures for arthritis of the feet and ankle Sports injuries and tendinopathies.</p>
      <p>Total ankle replacement and deformity correction of the foot and ankle.</p>
    </div>
  </div>

  <div class="panel contact">
    <div class="contact__top"><span class="brand brand--light"><span class="brand__dot"></span>Hollowbrook Clinic</span></div>
    <div class="contact__building ph" role="img" aria-label="Modern clinic building against a blue sky"></div>
    <div class="contact__logo"><span class="brand brand--dark"><span class="brand__dot"></span>Hollowbrook Clinic</span></div>
    <div class="contact__info">
      <div class="info-row">
        <svg viewBox="0 0 12 12" aria-hidden="true"><path d="M6 0a4 4 0 0 1 4 4c0 3-4 8-4 8S2 7 2 4a4 4 0 0 1 4-4z" fill="#fff"/><circle cx="6" cy="4" r="1.5" fill="var(--blue)"/></svg>
        <div><b>Hollowbrook Clinic</b>-Suite 304, Level 3<br>Harbourside Private Hospital<br>118-122 Marlow St Kestrel Bay NSW<br>-42 Ferry Road Tanby NSW</div>
      </div>
      <div class="info-row no-icon"><div>(02) 5550 1870<br>(02) 5550 1502</div></div>
      <div class="info-row">
        <svg viewBox="0 0 12 12" aria-hidden="true"><rect x="0.5" y="2" width="11" height="8" fill="#fff"/><path d="M0.5 2 6 7l5.5-5" stroke="var(--blue)" fill="none"/></svg>
        <div>info@hollowbrookclinic.com.au</div>
      </div>
      <div class="info-row">
        <svg viewBox="0 0 12 12" aria-hidden="true"><circle cx="6" cy="6" r="5.3" fill="none" stroke="#fff" stroke-width="1.2"/><path d="M0.7 6h10.6M6 0.7c-3 3-3 7.6 0 10.6M6 0.7c3 3 3 7.6 0 10.6" stroke="#fff" fill="none"/></svg>
        <div>www.hollowbrookclinic.com.au</div>
      </div>
    </div>
  </div>

  <div class="panel">
    <div class="cover__photo ph" role="img" aria-label="Runner holding a painful ankle, wearing a turquoise running shoe"></div>
    <div class="cover__hook"><strong>yes I have<br>a painful<br>ankle</strong><span>&amp; want to<br>find out<br>more...</span></div>
    <svg class="curves" viewBox="0 0 253 588" preserveAspectRatio="none" aria-hidden="true">
      <path d="M0 380 C80 390 180 350 253 280 L253 588 L0 588 Z" fill="var(--pale)"/>
      <path d="M0 395 C90 400 190 360 253 300 L253 588 L0 588 Z" fill="var(--aqua)"/>
      <path d="M0 410 C90 412 190 375 253 320 L253 588 L0 588 Z" fill="var(--blue)"/>
    </svg>
    <div class="cover__footer">
      <span class="brand brand--light"><span class="brand__dot"></span>Hollowbrook Clinic</span>
      <div class="cover__titles">My Painful Ankle<small>Solutions for Ankle Arthritis</small>Dr Martin Ellery<small>Orthopaedic Foot and Ankle Surgeon</small></div>
    </div>
  </div>
</section>

</body>
</html>
```